Design four banner ads for our upcoming revamped website

We need four banner ads for our website.

The link of our website is http://beta.mervatrade.com/

The banners will appear under the "Promotions" tab which is currently exhibiting placeholder images.

The titles for each of the banner ads are as follow:
1) Double Credit Chance
2) Capital Protection Scheme
3) Trade Bonus
4) 2.5% Annual Interest

Target Market(s)

forex traders

Requirements
Must have
• The banners must adhere and blend with the website existing theme
Should not have
• Please do not use any human figures in the banner or pictures of humans waving around cash.

```html
<!DOCTYPE html>
<html lang="en">
<head>
<meta charset="utf-8">
<title>Promotions Banners</title>
<link rel="stylesheet" href="https://fonts.googleapis.com/css2?family=Arimo:wght@400;700&display=swap">
<style>
  :root {
    --bg: #f1f1f1;
    --orange: #f5821f;
    --red: #c33535;
    --green: #5aae1c;
    --blue: #4a94c4;
    --white: #ffffff;
    --border: #dcdcdc;
  }
  html, body {
    margin: 0;
    padding: 0;
    overflow: hidden;
    background: var(--bg);
  }
  .canvas {
    position: relative;
    width: 1200px;
    height: 1200px;
    background: var(--bg);
    font-family: "Arimo", Arial, sans-serif;
    overflow: hidden;
  }
  .swatch {
    position: absolute;
    left: 34px;
    width: 53px;
    height: 150px;
  }
  .swatch--orange { top: 36px; background: var(--orange); }
  .swatch--red { top: 204px; background: var(--red); }
  .swatch--green { top: 369px; background: var(--green); }
  .swatch--blue { top: 534px; background: var(--blue); }

  .banner {
    position: absolute;
    left: 306px;
    width: 587px;
    height: 255px;
    display: block;
  }
  .banner--credit { top: 63px; }
  .banner--protection { top: 334px; }
  .banner--bonus { top: 607px; }
  .banner--interest { top: 880px; }

  .banner text {
    font-family: "Arimo", Arial, sans-serif;
  }
  .headline { font-weight: 700; font-size: 27px; }
  .headline--white { fill: var(--white); }
  .headline--red { fill: var(--red); }
  .rate { font-weight: 700; font-size: 26px; fill: var(--blue); }
  .interest-label { font-weight: 400; font-size: 26px; fill: var(--white); }
  .dollar { font-weight: 400; font-size: 32px; fill: var(--white); }
  .tick {
    fill: none;
    stroke: var(--white);
    stroke-width: 13;
    stroke-linecap: round;
    stroke-linejoin: round;
  }
</style>
</head>
<body>
<main class="canvas">
  <div class="swatch swatch--orange"></div>
  <div class="swatch swatch--red"></div>
  <div class="swatch swatch--green"></div>
  <div class="swatch swatch--blue"></div>

  <svg class="banner banner--credit" viewBox="0 0 391 170" aria-label="Double Credit Chance">
    <rect x="0" y="0" width="391" height="170" fill="var(--white)"/>
    <rect x="0" y="0" width="391" height="77" fill="var(--green)"/>
    <rect x="0" y="94" width="391" height="76" fill="var(--blue)"/>
    <text class="headline headline--white" x="33" y="53">Double</text>
    <text class="headline headline--white" x="150" y="138">Credit Chance</text>
    <polyline class="tick" points="62,108 90,148 246,20"/>
  </svg>

  <svg class="banner banner--protection" viewBox="0 0 391 170" aria-label="Capital Protection Scheme">
    <rect x="0.5" y="0.5" width="390" height="169" fill="var(--white)" stroke="var(--border)"/>
    <polygon class="lock-badge" fill="var(--red)"
      points="96,31 146,55 152,106 113,133 63,115 57,61"/>
    <circle cx="104" cy="67" r="11" fill="var(--white)"/>
    <polygon points="99,72 109,72 114,110 94,110" fill="var(--white)"/>
    <text class="headline headline--red" x="183" y="64">Capital</text>
    <text class="headline headline--red" x="183" y="95">Protection</text>
    <text class="headline headline--red" x="183" y="126">Scheme</text>
  </svg>

  <svg class="banner banner--bonus" viewBox="0 0 391 170" aria-label="Trade Bonus">
    <rect x="0.5" y="0.5" width="390" height="169" fill="var(--white)" stroke="var(--border)"/>
    <polygon class="arrow-bonus" fill="var(--orange)"
      points="391,42 226,42 226,19 179,65 226,112 226,89 391,89"/>
    <polygon class="arrow-trade" fill="var(--orange)"
      points="0,90 166,90 166,67 213,113 166,160 166,137 0,137"/>
    <text class="headline headline--white" x="226" y="76">Bonus</text>
    <text class="headline headline--white" x="83" y="124">Trade</text>
  </svg>

  <svg class="banner banner--interest" viewBox="0 0 391 170" aria-label="2.5% Annual Interest">
    <rect x="0" y="0" width="391" height="170" fill="var(--blue)"/>
    <polygon class="rate-badge" fill="var(--white)"
      points="75,27 126,47 132,99 95,128 44,107 38,55"/>
    <text class="rate" x="85" y="88" text-anchor="middle">2.5%</text>
    <text class="dollar" x="194" y="88">$</text>
    <g class="growth-bars" fill="var(--white)">
      <rect x="218" y="63" width="9" height="27"/>
      <rect x="230" y="56" width="9" height="34"/>
      <rect x="242" y="48" width="9" height="42"/>
      <rect x="254" y="38" width="9" height="52"/>
      <rect x="266" y="28" width="9" height="62"/>
    </g>
    <text class="interest-label" x="154" y="120">Annual Interest</text>
  </svg>
</main>
</body>
</html>
```